I need an out door banner to help me promote my classes, i am a dating coach. i would like to see designs that use the colors. black, yellow, pink, white,orange. colors that attract women. the final design should communicate how women can Reclaim Every Spark, Shine Once More.

Target Market(s)

Bright Mornings After Midnight Storms: Reclaim Every Spark, Shine Once More: Heartfelt Wisdom on Modern Courtship

Industry/Entity Type

dating advice

Logo Text

Attention Ladies: Bright Mornings the Narcissist, the abusers, the couch potatoes, the players & the losers...( Expose & Dump his #ss before he destroys your life)

Colors

Designer to choose colors to be used in the design.

Requirements
Nice to have
• Some bold text too
Should not have
• black round

```html
<!DOCTYPE html>
<html lang="en">
<head>
<meta charset="utf-8">
<title>Bright Mornings – Outdoor Banner</title>
<link href="https://fonts.googleapis.com/css2?family=Open+Sans:wght@700;800&family=Roboto:wght@300;500;700;900&family=Roboto+Condensed:wght@500&display=swap" rel="stylesheet">
<style>
  :root {
    --stage: #1b1b1d;
    --white: #ffffff;
    --pink: #e8038f;
    --yellow: #f6ee1f;
    --ink: #1c1c1c;
    --orange: #f39a1e;
    --red: #e2231a;
  }
  * { margin: 0; padding: 0; box-sizing: border-box; }
  html, body { width: 1200px; height: 1000px; overflow: hidden; background: var(--stage); }
  .canvas {
    width: 1200px; height: 1000px;
    display: flex; align-items: center; justify-content: center;
  }
  .banner {
    width: 560px; height: 930px;
    background: var(--white);
    display: flex; flex-direction: column;
    overflow: hidden;
  }
  .brand-area {
    height: 270px;
    display: flex; flex-direction: column; align-items: center; justify-content: center;
    gap: 14px;
  }
  .brand-mark { display: flex; align-items: center; gap: 14px; }
  .brand-dot {
    width: 22px; height: 22px; border-radius: 50%;
    background: var(--pink);
  }
  .brand-name {
    font-family: "Open Sans", sans-serif;
    font-weight: 800;
    font-size: 54px;
    color: var(--ink);
    letter-spacing: -0.5px;
  }
  .brand-tagline {
    font-family: "Open Sans", sans-serif;
    font-weight: 700;
    font-size: 13px;
    color: var(--pink);
  }
  .message {
    flex: 1;
    background: var(--pink);
    padding: 52px 50px 40px 52px;
    color: var(--white);
  }
  .headline {
    font-family: "Roboto", sans-serif;
    font-weight: 900;
    font-size: 42px;
    line-height: 1.1;
  }
  .subline {
    font-family: "Roboto", sans-serif;
    font-weight: 300;
    font-size: 38px;
    line-height: 1.25;
    margin-top: 6px;
  }
  .callout {
    display: flex; align-items: center; gap: 18px;
    margin-top: 42px;
  }
  .callout-badge {
    font-family: "Roboto", sans-serif;
    font-weight: 700;
    font-size: 17px;
    color: var(--ink);
    background: var(--yellow);
    border: 3px solid var(--red);
    border-radius: 20px;
    padding: 7px 16px;
  }
  .callout-name {
    font-family: "Open Sans", sans-serif;
    font-weight: 800;
    font-size: 34px;
  }
  .warning-list {
    list-style: none;
    margin: 40px 0 0 62px;
    display: flex; flex-direction: column; gap: 22px;
  }
  .warning-item {
    display: flex; align-items: center; gap: 16px;
    font-family: "Roboto", sans-serif;
    font-weight: 500;
    font-size: 24px;
  }
  .warning-icon { width: 32px; height: 32px; flex: none; }
  .class-info {
    height: 110px;
    background: var(--yellow);
    display: flex; flex-direction: column; align-items: center; justify-content: center;
    font-family: "Roboto Condensed", sans-serif;
    font-weight: 500;
    font-size: 25px;
    line-height: 1.35;
    color: var(--ink);
    text-align: center;
  }
</style>
</head>
<body>
<main class="canvas">
  <section class="banner">
    <header class="brand-area">
      <div class="brand-mark">
        <span class="brand-dot"></span>
        <span class="brand-name">Bright Mornings</span>
      </div>
      <p class="brand-tagline">Expose &amp; Dump his #ss before he destroys your life</p>
    </header>

    <div class="message">
      <h1 class="headline">Reclaim Every Spark,</h1>
      <p class="subline">Shine Once More</p>

      <div class="callout">
        <span class="callout-badge">!Attention Ladies</span>
        <span class="callout-name">Bright Mornings</span>
      </div>

      <ul class="warning-list">
        <li class="warning-item"><svg class="warning-icon" viewBox="0 0 32 32"><circle cx="16" cy="16" r="13" fill="none" stroke="#fff" stroke-width="2.5"/><path d="M11 11 L21 21 M21 11 L11 21" stroke="#fff" stroke-width="2.5" stroke-linecap="round"/></svg>The Narcissist</li>
        <li class="warning-item"><svg class="warning-icon" viewBox="0 0 32 32"><circle cx="16" cy="16" r="13" fill="none" stroke="#fff" stroke-width="2.5"/><path d="M11 11 L21 21 M21 11 L11 21" stroke="#fff" stroke-width="2.5" stroke-linecap="round"/></svg>The abusers</li>
        <li class="warning-item"><svg class="warning-icon" viewBox="0 0 32 32"><circle cx="16" cy="16" r="13" fill="none" stroke="#fff" stroke-width="2.5"/><path d="M11 11 L21 21 M21 11 L11 21" stroke="#fff" stroke-width="2.5" stroke-linecap="round"/></svg>The couch potatoes</li>
        <li class="warning-item"><svg class="warning-icon" viewBox="0 0 32 32"><circle cx="16" cy="16" r="13" fill="none" stroke="#fff" stroke-width="2.5"/><path d="M11 11 L21 21 M21 11 L11 21" stroke="#fff" stroke-width="2.5" stroke-linecap="round"/></svg>The players</li>
        <li class="warning-item"><svg class="warning-icon" viewBox="0 0 32 32"><circle cx="16" cy="16" r="13" fill="none" stroke="#fff" stroke-width="2.5"/><path d="M11 11 L21 21 M21 11 L11 21" stroke="#fff" stroke-width="2.5" stroke-linecap="round"/></svg>The losers</li>
      </ul>
    </div>

    <footer class="class-info">
      <p>FREE CLASSES EVERY WED@ 12AM</p>
      <p>4820 LARKIN AVE WALK-INS EXCEPTED</p>
    </footer>
  </section>
</main>
</body>
</html>
```